Consultative Employee Benifits Firm Needs Business Card Design Project

We need a business card design for a new company based in Northern Virginia called "Telman Financial Services, LLC. We are both a wealth management advisory firm, as well as an employee benefits firm, which strives to provide superior creativity in employee benefits plan design and greater client and employee satisfaction. We are obsessed with service and follow up.

Our firm specializes in the areas of group health, life, dental, disability, voluntary benefits, Executive Benefits, HRA and HSA programs. We offer competitive employee benefit packages and pricing models for single or multi-state/multi location companies by maintaining preferred relationships with a large number of regional and national carriers.

Our firm also considers the many dimensions of your wealth through an integrated process we call wealth structuring — a comprehensive, dynamic approach to building, preserving, enjoying and transferring your wealth. And because we are often dealing with complex ownership structures and complicated, changing family dynamics, we bring the highest level of experience and creativity to managing your wealth. We work hard to help ensure that your legacy lasts by preparing your children for the financial challenges and opportunities that are headed their way.

Our final design should communicate an integrated approach to finanial safety and optimization
Updates

 Due to a few designers not accepting due to low budget, I have increased budget payout 19%. 

Project Deadline Extended
Reason: I have only heard from 12 designers. So, maybe I did not give the right amount of time to do the project. For the designers that have submitted their designs, thank you. I have seen three or four designs that I liked and might end up with one of them after it's all over, but I thought I would see between 20 - 25 before everything was over. Dan

Target Market(s)

Professionals; doctors, contractors, small to mid size business owners, ages 50 -65 with nert worth of 2MM

Industry/Entity Type

Financial

Requirements
Must have
• Telman Financial Services, LLC

Dan Telman
President
41957 Marwick Hollow Street
Quenford Glen, 20871

Office: 703 555-0184
Cell: 703 555-0127
Fax: 703 555-0163
Email: dantelman@quorvex.net
Should not have
• No pink or yellow colors.
No generic clipart (coins, dollar signs, money bags, graphs)

```html
<!DOCTYPE html>
<html lang="en">
<head>
<meta charset="utf-8">
<title>Telman Financial Services, LLC — Business Card</title>
<link rel="stylesheet" href="https://fonts.googleapis.com/css2?family=Source+Sans+3:ital,wght@0,400;0,600;0,700;1,700&display=swap">
<style>
  :root {
    --navy: #222f5e;
    --green: #6cb33f;
    --paper: #f1efea;
    --page: #ffffff;
    --white: #ffffff;
  }
  * { box-sizing: border-box; margin: 0; padding: 0; }
  html, body {
    width: 1200px;
    height: 900px;
    overflow: hidden;
    background: var(--page);
    font-family: "Source Sans 3", "Myriad Pro", Arial, sans-serif;
  }
  .stage { position: relative; width: 1200px; height: 900px; }

  .card {
    position: absolute;
    width: 510px;
    height: 288px;
    background: var(--paper);
    overflow: hidden;
    box-shadow: 0 2px 6px rgba(0,0,0,0.18);
  }
  .card--front { left: 150px; top: 150px; }
  .card--back  { left: 540px; top: 470px; border-top-right-radius: 18px; }

  .card__shape { position: absolute; inset: 0; width: 510px; height: 288px; }

  .brand {
    position: absolute;
    display: flex;
    align-items: center;
    gap: 10px;
  }
  .brand__dot {
    width: 30px;
    height: 30px;
    border-radius: 50%;
    background: var(--green);
    flex: none;
  }
  .brand__name {
    color: var(--navy);
    font-weight: 600;
    font-size: 21px;
    line-height: 1.05;
    width: 170px;
  }
  .card--front .brand { left: 36px; top: 112px; }
  .card--back .brand  { left: 300px; top: 150px; }

  .contact {
    position: absolute;
    right: 18px;
    top: 84px;
    text-align: right;
    color: var(--white);
    font-size: 14.5px;
    line-height: 19.5px;
  }
  .contact__name { font-weight: 700; font-size: 15.5px; }
  .contact__title { color: var(--green); font-weight: 700; font-style: italic; }
  .contact__lines { margin-top: 10px; line-height: 17.5px; }
</style>
</head>
<body>
<main class="stage">

  <section class="card card--front" aria-label="Card front">
    <svg class="card__shape" viewBox="0 0 510 288" aria-hidden="true">
      <path d="M510 0 C330 18 222 140 222 288 L510 288 Z" fill="var(--navy)"/>
      <path d="M510 0 C330 18 222 140 222 288" fill="none" stroke="var(--green)" stroke-width="4"/>
    </svg>
    <div class="brand">
      <span class="brand__dot"></span>
      <span class="brand__name">Telman Financial Services, LLC</span>
    </div>
    <address class="contact" style="font-style:normal">
      <div class="contact__name">Dan Telman</div>
      <div class="contact__title">President</div>
      <div>41957 Marwick Hollow Street</div>
      <div>Quenford Glen, 20871</div>
      <div class="contact__lines">
        <div>Office: 703 555-0184</div>
        <div>Cell: 703 555-0127</div>
        <div>Fax: 703 555-0163</div>
        <div>dantelman@quorvex.net</div>
      </div>
    </address>
  </section>

  <section class="card card--back" aria-label="Card back">
    <svg class="card__shape" viewBox="0 0 510 288" aria-hidden="true">
      <rect width="510" height="288" fill="var(--navy)"/>
      <path d="M510 24 C380 26 250 120 236 288 L510 288 Z" fill="var(--paper)"/>
      <path d="M510 24 C380 26 250 120 236 288" fill="none" stroke="var(--green)" stroke-width="4"/>
    </svg>
    <div class="brand">
      <span class="brand__dot"></span>
      <span class="brand__name">Telman Financial Services, LLC</span>
    </div>
  </section>

</main>
</body>
</html>
```